Brightway Inc. Business Card Design

Brightway Inc. is in search of a great clean design for our business cards!

Looking to incorporate our full logo and watermark on side one (however, I am open to having the text and watermark separated within the design.)

On side two, I am looking to have contact information (Name, Position, Phone #, Email, Website (www.thebrightway.ca). Can have the logo and/or watermark as part of the design if applicable.

Please add tagline "Where Shine Counts" on either side 1 or 2. This tagline can be in a sans serif, serif or cursive font as long as it compliments overall design. Capitalization can be title or sentence case depending on how it fits within the design.

Get creative!! Looking for a clean, crisp, premium design! Looking for a glossy card finish with spot UV features when printed. Cards will also be printed with rounded corners. Standard dimensions (3.5 x 2).

Target Market(s)

B2B - primary clients are business owners or property management corporations. (residential jobs are few and far between)

Industry/Entity Type

Business

Contact Information for Business Card

- clean, crisp design
- double sided
- spot UV accents and glossy finish upon printing
- standard business card size (3.5 x 2) with rounded corners
- please see project description for requirements per side

Font styles to use
Sans Serif

Requirements
Must have
• - adequate bleeds with print ready files
• - cohesive design elements between side 1 & 2
• - spot UV elements (can be on both sides or just one, use your discretion)
• - colour pallet should match the logo file provided
• - incorporate tagline "where shine counts" (this tagline can be in a serif or sans serif font as long as it is complimentary to the overall design.
Nice to have
• - Premium elements with a clean design
Should not have
• - Please omit cartoon or whimsical like designs, think premium.
• - Colours should not stray from the pallet of the provided logo.

```html
<!DOCTYPE html>
<html lang="en">
<head>
<meta charset="utf-8">
<title>Brightway Inc. Business Cards</title>
<link href="https://fonts.googleapis.com/css2?family=Montserrat:wght@500;600;700;800&display=swap" rel="stylesheet">
<style>
  :root {
    --navy: #1b2560;
    --navy-light: #2a3478;
    --teal: #1fbcbc;
    --teal-light: #3fd2cf;
    --white: #ffffff;
    --paper: #f3f3f3;
    --ink: #3a3d48;
    --backdrop: #2b2b2d;
  }
  * { margin: 0; padding: 0; box-sizing: border-box; }
  html, body {
    width: 1200px; height: 834px; overflow: hidden;
    background: var(--backdrop);
    font-family: "Montserrat", sans-serif;
  }
  .stage { position: relative; width: 1200px; height: 834px; }
  .card {
    position: absolute; width: 560px; height: 320px;
    border-radius: 14px; overflow: hidden;
    box-shadow: 0 12px 30px rgba(0,0,0,.45);
  }
  /* Side one */
  .card-front {
    left: 170px; top: 60px;
    background: radial-gradient(ellipse at 45% 40%, var(--navy-light), var(--navy) 70%);
  }
  .card-front .wave { position: absolute; inset: 0; width: 100%; height: 100%; }
  .brand {
    position: absolute; display: flex; align-items: center; gap: 12px;
    font-weight: 800; letter-spacing: .5px; white-space: nowrap;
  }
  .brand-mark { display: block; background: var(--teal); }
  .card-front .brand { left: 120px; top: 104px; color: var(--white); font-size: 40px; }
  .card-front .brand-mark { width: 40px; height: 40px; }
  .tagline {
    position: absolute; right: 62px; bottom: 20px;
    color: var(--navy); font-weight: 600; font-size: 15px;
  }
  /* Side two */
  .card-back {
    left: 470px; top: 454px;
    background: linear-gradient(120deg, var(--white), var(--paper));
  }
  .card-back .brand { right: 36px; top: 52px; color: var(--navy); font-size: 30px; }
  .card-back .brand-mark { width: 30px; height: 30px; }
  .accent-bar {
    position: absolute; left: 0; top: 148px; width: 10px; height: 120px;
    background: var(--teal);
  }
  .contact { position: absolute; left: 46px; top: 150px; color: var(--ink); }
  .person-name { font-size: 17px; font-weight: 700; }
  .person-role { font-size: 14px; font-weight: 500; color: var(--teal); margin-bottom: 12px; }
  .contact-list { list-style: none; font-size: 13px; font-weight: 500; }
  .contact-list li { display: flex; align-items: center; gap: 10px; margin-bottom: 7px; }
  .contact-list svg { width: 14px; height: 14px; flex: none; }
</style>
</head>
<body>
<main class="stage">
  <section class="card card-front" aria-label="Card side one">
    <svg class="wave" viewBox="0 0 560 320" preserveAspectRatio="none" aria-hidden="true">
      <path d="M0,262 Q320,250 560,150 L560,320 L0,320 Z" fill="var(--white)"/>
      <path d="M0,272 Q322,262 560,162 L560,320 L0,320 Z" fill="var(--teal)"/>
    </svg>
    <div class="brand"><span class="brand-mark"></span>BRIGHTWAY INC.</div>
    <p class="tagline">Where Shine Counts</p>
  </section>

  <section class="card card-back" aria-label="Card side two">
    <div class="brand"><span class="brand-mark"></span>BRIGHTWAY INC.</div>
    <span class="accent-bar"></span>
    <div class="contact">
      <p class="person-name">Alex Marlow</p>
      <p class="person-role">President</p>
      <ul class="contact-list">
        <li>
          <svg viewBox="0 0 24 24" fill="none" stroke="var(--teal)" stroke-width="2"><path d="M5 3h4l2 5-3 2a11 11 0 0 0 6 6l2-3 5 2v4a2 2 0 0 1-2 2A18 18 0 0 1 3 5a2 2 0 0 1 2-2z"/></svg>
          555-204-7719
        </li>
        <li>
          <svg viewBox="0 0 24 24" fill="none" stroke="var(--teal)" stroke-width="2"><rect x="3" y="5" width="18" height="14"/><path d="M3 5l9 8 9-8"/></svg>
          info@thebrightway.ca
        </li>
        <li>
          <svg viewBox="0 0 24 24" fill="none" stroke="var(--teal)" stroke-width="2"><circle cx="12" cy="12" r="9"/><path d="M3 12h18M12 3c3 3 3 15 0 18M12 3c-3 3-3 15 0 18"/></svg>
          www.thebrightway.ca
        </li>
      </ul>
    </div>
  </section>
</main>
</body>
</html>
```